Flyer Design sales and lettings

We need a double sided flyer for our Estate and Letting agency. We have just moved in to 16th century office and expanded our offer to commercial and residential sales (previously we were targeted on lettings only). We are based in small rural town in Midlands, UK.Any photos, graphics will need to be linked to our location (please dont use skyscrapers :)One side of our flyer will have to treat about lettings and our offer - 7% plus vat commission on all new lettings, no extra costs, rent guarantee insurance, we are open 6 days a week and available 24/7.Please insert information about our commercial department on this side as well. "Landlords! Did you know that we also do commercial lettings? Call us on 01592738164 for best offer in the area. Other side informing clients about our sales offer 0.7% plus vat on all new sales instructions, free market appraisal, no up front costs, no sale no fee, we are open 6 days a week and available 24/7Here is our website: www.hollowbrookhomes.uk We are members of KLT, WMA and leasewell (logos attached)Thank you Tomasz Welbarek

Target Market(s)

Landlords and vendors in local area

Industry/Entity Type

Real Estate Agent

Font styles to use
Decorative
Script

Requirements
Must have
• all points stated in descriptip
Nice to have
• our logo or parts of it incorporated in design, elegant retro, stylish effcts.
• Silver/Charcoal coulour with retro gold theme.
Should not have
• modern, city accents.

```html
<!DOCTYPE html>
<html lang="en">
<head>
<meta charset="utf-8">
<title>Hollowbrook Homes – Lettings Flyer</title>
<link href="https://fonts.googleapis.com/css2?family=Lato:wght@400;700;900&display=swap" rel="stylesheet">
<style>
  :root {
    --backdrop: #e4e4e4;
    --charcoal: #3b3b3d;
    --charcoal-deep: #2f2f31;
    --gold: #e8ac33;
    --gold-deep: #e3902c;
    --silver: #ececec;
    --white: #ffffff;
    --ink: #2b2b2b;
    --blue: #4a78b5;
  }
  * { box-sizing: border-box; margin: 0; padding: 0; }
  html, body { width: 1200px; height: 926px; overflow: hidden; }
  body { background: var(--backdrop); font-family: "Lato", Arial, sans-serif; position: relative; }

  .flyer {
    position: absolute; left: 282px; top: 18px;
    width: 600px; height: 840px;
    transform: scale(1.06); transform-origin: top left;
    background: var(--silver); overflow: hidden;
    box-shadow: 0 4px 14px rgba(0,0,0,.18);
  }
  .layer { position: absolute; left: 0; top: 0; }

  .hero-photo {
    position: absolute; left: 0; top: 0; width: 600px; height: 318px;
    background: linear-gradient(160deg, #c9d3dc 0%, #a9a089 35%, #6f6246 65%, #3e3a30 100%);
  }

  .brand { position: absolute; left: 36px; top: 58px; color: var(--white); }
  .brand-mark { display: flex; align-items: center; gap: 8px; font-size: 13px; font-weight: 700; margin-bottom: 30px; }
  .brand-mark::before { content: ""; width: 14px; height: 14px; border-radius: 50%; background: var(--white); }
  .brand-name { font-size: 25px; font-weight: 900; line-height: 30px; letter-spacing: .2px; }
  .brand-tagline { margin-top: 10px; color: var(--ink); font-size: 13.5px; line-height: 17px; }

  .services { position: absolute; left: 0; top: 303px; width: 600px; height: 230px; }
  .service { position: absolute; top: 0; height: 230px; text-align: center; color: var(--white); }
  .service--commercial { left: 18px; width: 170px; }
  .service--residential { left: 193px; width: 210px; background: var(--gold); color: var(--ink); padding: 0 12px; }
  .service--guide { left: 412px; width: 172px; }
  .service-icon {
    width: 50px; height: 50px; border-radius: 50%; background: var(--white);
    margin: 30px auto 10px; display: flex; align-items: center; justify-content: center;
  }
  .service-title { font-size: 12.5px; line-height: 15px; text-transform: uppercase; margin-bottom: 10px; }
  .service-text { font-size: 9px; line-height: 11.6px; text-align: justify; text-align-last: center; padding: 0 14px; }
  .service--residential .service-text { padding: 0; color: var(--white); }
  .service-lead { font-size: 9.5px; text-transform: uppercase; margin-bottom: 16px; padding: 0 10px; }

  .offer { position: absolute; left: 290px; top: 556px; width: 290px; text-align: center; color: var(--ink); font-weight: 700; }
  .offer-head { font-size: 21px; font-weight: 900; line-height: 24px; }
  .offer-head .accent { color: var(--blue); }
  .offer-body { font-size: 13.5px; line-height: 17.5px; text-transform: uppercase; }

  .hours { position: absolute; left: 20px; top: 678px; width: 330px; text-align: center; color: var(--gold); font-size: 18px; font-weight: 900; line-height: 23px; }
  .hours .hl { color: var(--white); }

  .commercial-cta { position: absolute; left: 0; top: 768px; width: 600px; text-align: center; color: var(--white); font-size: 13.5px; font-weight: 900; line-height: 17px; }
  .commercial-cta .hl { color: var(--gold); }
</style>
</head>
<body>
<main class="flyer">
  <div class="hero-photo" role="img" aria-label="Photograph of a historic sandstone town building with a street lamp, seen from below against a cloudy sky"></div>

  <svg class="layer" width="600" height="840" viewBox="0 0 600 840" aria-hidden="true">
    <polygon points="0,0 172,0 286,156 112,318 0,318" fill="var(--gold)" opacity=".86"/>
    <rect x="0" y="318" width="600" height="202" fill="var(--charcoal)"/>
    <rect x="0" y="520" width="600" height="320" fill="var(--silver)"/>
    <path d="M0,568 L330,650 Q360,660 385,690 L430,726 L600,700 L600,840 L0,840 Z" fill="var(--charcoal)"/>
    <polygon points="0,520 132,520 215,620 0,568" fill="var(--gold)"/>
    <polygon points="132,520 215,620 160,600" fill="var(--gold-deep)"/>
    <polygon points="0,692 56,840 0,840" fill="var(--gold)"/>
  </svg>

  <header class="brand">
    <div class="brand-mark">Hollowbrook Homes</div>
    <h1 class="brand-name">THE HOLLOWBROOK<br>HOMES</h1>
    <p class="brand-tagline">RESIDENTIAL &amp; COMMERCIAL<br>&nbsp;SALES &amp; LETTINGS</p>
  </header>

  <section class="services">
    <article class="service service--commercial">
      <div class="service-icon">
        <svg width="30" height="30" viewBox="0 0 30 30" aria-hidden="true">
          <rect x="5" y="6" width="9" height="20" fill="var(--charcoal)"/>
          <rect x="14" y="2" width="8" height="24" fill="var(--charcoal)"/>
          <rect x="22" y="12" width="5" height="14" fill="var(--charcoal)"/>
          <g fill="var(--white)"><rect x="7" y="9" width="2" height="2"/><rect x="10" y="9" width="2" height="2"/><rect x="7" y="14" width="2" height="2"/><rect x="10" y="14" width="2" height="2"/><rect x="16" y="6" width="2" height="2"/><rect x="16" y="11" width="2" height="2"/><rect x="16" y="16" width="2" height="2"/><rect x="24" y="15" width="2" height="2"/></g>
        </svg>
      </div>
      <h2 class="service-title">Commercial properties<br>to let</h2>
      <p class="service-text">With an extensive knowledge of the property market we are dedicated to finding the perfect property solution for investors, tenants, landlords, buyers and sellers alike.</p>
    </article>

    <article class="service service--residential">
      <div class="service-icon">
        <svg width="26" height="26" viewBox="0 0 26 26" aria-hidden="true">
          <path d="M13 3 L24 13 L21 13 L21 23 L15 23 L15 17 L11 17 L11 23 L5 23 L5 13 L2 13 Z" fill="var(--charcoal)"/>
        </svg>
      </div>
      <h2 class="service-title">Residential properties<br>to let</h2>
      <p class="service-text">We are a unique property company offering a professional service whilst adopting a personal approach. Our services can be tailored to handle your requirements in every aspect of the property market.</p>
    </article>

    <article class="service service--guide">
      <div class="service-icon">
        <svg width="26" height="30" viewBox="0 0 26 30" aria-hidden="true">
          <path d="M5 3 L19 3 L19 27 L5 27 Z" fill="none" stroke="var(--charcoal)" stroke-width="2.5"/>
          <path d="M9 6 L22 4 L22 26 L9 28 Z" fill="var(--charcoal)"/>
        </svg>
      </div>
      <h2 class="service-title">Landlords guide</h2>
      <p class="service-text service-lead">No let no fee for landlords</p>
      <p class="service-text">We never charge for any of our services upfront so you can be confident you are getting the best service possible.</p>
    </article>
  </section>

  <section class="offer">
    <p class="offer-head"><span class="accent">OUR</span> OFFER - <span class="accent">7%</span> PLUS</p>
    <p class="offer-body">VAT commission<br>on all new lettings, no extra<br>costs, rent guarantee insurance</p>
  </section>

  <p class="hours">WE ARE OPEN <span class="hl">6</span> DAYS A WEEK<br>AND AVAILABLE <span class="hl">24/7.</span></p>

  <p class="commercial-cta">LANDLORDS! DID YOU KNOW THAT WE ALSO DO <span class="hl">COMMERCIAL LETTINGS?</span><br>CALL US ON <span class="hl">01592738164</span> FOR BEST OFFER IN THE AREA.</p>
</main>
</body>
</html>
```